Morvek Menu

Hi there,
My restaurant called "Morvek" means Spice in hebrew.
We are middle eastern restaurant that specialist in dips,salads and hot bread baked on the spot and charcoal grilled meat skewers
The restaurant is pretty casual and the atmosphere is nice and customers feels like home.
on www.morvek.com.au you can see photos of the restaurant and the food.
ill add up the menus that i would like to be design please and the logo that is on the front of the shop is been add up
thank you

Target Market(s)

The regulars of the restaurant is jewish/israelis

Industry/Entity Type

Restaurant

```html
<!DOCTYPE html>
<html lang="en">
<head>
<meta charset="utf-8">
<title>Morvek — Dinner Menu</title>
<link rel="stylesheet" href="https://fonts.googleapis.com/css2?family=Cormorant+Garamond:wght@500&family=Lobster&family=Alegreya+SC:wght@800&display=swap">
<style>
  :root {
    --page: #ffffff;
    --maroon: #6e2b2c;
    --maroon-deep: #5c2122;
    --maroon-soft: #7d3a37;
    --vine-gold: #dcc493;
    --vine-shade: #c4a267;
    --stripe-gold: #f6c21a;
    --stripe-pale: #fff0b0;
    --band-top: #e8463a;
    --band-mid: #f28a2a;
    --band-low: #fcc214;
    --ornament: #8a4a2a;
    --ornament-soft: #a5622f;
    --plate: #3e2c29;
    --plate-ring: #c9a56a;
    --cutlery: #d5b07a;
    --ink-dark: #5a1c1e;
    --ink-light: #ffffff;
    --ink-list: #1c0f0c;
  }
  * { margin: 0; padding: 0; box-sizing: border-box; }
  html, body { width: 878px; height: 1200px; overflow: hidden; background: var(--page); }
  .menu-cover {
    position: relative;
    width: 878px; height: 1200px;
    overflow: hidden;
    background: var(--page);
  }
  .cover-field {
    position: absolute; left: 30px; top: 15px; width: 818px; height: 1170px;
    background:
      radial-gradient(circle at 120px 160px, var(--maroon-soft) 0, rgba(125,58,55,0) 110px),
      radial-gradient(circle at 700px 300px, var(--maroon-soft) 0, rgba(125,58,55,0) 120px),
      radial-gradient(circle at 110px 560px, var(--maroon-soft) 0, rgba(125,58,55,0) 120px),
      radial-gradient(circle at 720px 720px, var(--maroon-soft) 0, rgba(125,58,55,0) 120px),
      radial-gradient(circle at 120px 980px, var(--maroon-soft) 0, rgba(125,58,55,0) 120px),
      radial-gradient(circle at 700px 1080px, var(--maroon-soft) 0, rgba(125,58,55,0) 110px),
      linear-gradient(180deg, var(--maroon) 0%, var(--maroon-deep) 100%);
  }
  .vine-border {
    position: absolute; top: 15px; width: 34px; height: 1170px;
    background: linear-gradient(90deg, var(--vine-shade), var(--vine-gold) 50%, var(--vine-shade));
  }
  .vine-border--left { left: 238px; }
  .vine-border--right { left: 613px; }
  .gold-stripe {
    position: absolute; top: 15px; height: 1170px; width: 14px;
    background: linear-gradient(90deg, var(--stripe-gold) 0%, var(--stripe-gold) 55%, var(--stripe-pale) 100%);
  }
  .gold-stripe--left { left: 288px; }
  .gold-stripe--right { left: 580px; transform: scaleX(-1); }
  .spice-band {
    position: absolute; left: 304px; top: 15px; width: 272px; height: 1170px;
    background: linear-gradient(200deg, var(--band-top) 0%, var(--band-mid) 40%, var(--band-low) 85%);
  }
  .band-ornament {
    position: absolute; left: 340px; width: 205px;
    background: linear-gradient(180deg, var(--ornament-soft), var(--ornament));
    opacity: 0.8;
  }
  .band-ornament--top {
    top: 22px; height: 162px;
    border-radius: 50% 50% 45% 45% / 70% 70% 30% 30%;
  }
  .band-ornament--lower {
    top: 382px; height: 165px;
    border-radius: 45% 45% 50% 50% / 35% 35% 65% 65%;
  }
  .brand-name {
    position: absolute; left: 304px; width: 272px; top: 216px;
    text-align: center;
    font-family: "Cormorant Garamond", serif;
    font-weight: 500; font-size: 50px; line-height: 60px; color: var(--ink-light);
  }
  .brand-rule {
    position: absolute; left: 348px; width: 194px; height: 2px;
    background: var(--ink-light);
  }
  .brand-rule--upper { top: 292px; }
  .brand-rule--lower { top: 350px; }
  .menu-emblem { position: absolute; left: 0; top: 0; }
  .menu-title {
    font-family: "Lobster", cursive;
    font-size: 50px; fill: var(--ink-dark);
  }
  .course-list {
    position: absolute; left: 270px; width: 340px; top: 1004px;
    text-align: center;
    font-family: "Alegreya SC", serif; font-weight: 800;
    font-size: 21px; line-height: 23px; color: var(--ink-list);
  }
</style>
</head>
<body>
<main class="menu-cover">
  <div class="cover-field" role="img" aria-label="Maroon field with faint floral damask pattern"></div>
  <div class="vine-border vine-border--left" role="img" aria-label="Gold scrolling vine border"></div>
  <div class="vine-border vine-border--right" role="img" aria-label="Gold scrolling vine border"></div>
  <div class="gold-stripe gold-stripe--left"></div>
  <div class="gold-stripe gold-stripe--right"></div>
  <div class="spice-band"></div>
  <div class="band-ornament band-ornament--top" role="img" aria-label="Brown filigree flourish"></div>
  <div class="band-ornament band-ornament--lower" role="img" aria-label="Brown filigree flourish"></div>

  <h1 class="brand-name">Morvek</h1>
  <div class="brand-rule brand-rule--upper"></div>
  <div class="brand-rule brand-rule--lower"></div>

  <svg class="menu-emblem" width="878" height="1200" viewBox="0 0 878 1200">
    <defs>
      <path id="title-arc" d="M 294 668 A 240 240 0 0 1 602 668"/>
    </defs>
    <text class="menu-title"><textPath href="#title-arc" startOffset="50%" text-anchor="middle" textLength="300" lengthAdjust="spacingAndGlyphs">Dinner Menu</textPath></text>
    <g class="plate">
      <circle cx="440" cy="787" r="146" fill="var(--plate)"/>
      <circle cx="440" cy="787" r="138" fill="none" stroke="var(--plate-ring)" stroke-width="1.5"/>
    </g>
    <g class="cutlery" fill="var(--cutlery)">
      <path d="M362 708 h5 v36 h4 v-36 h5 v36 h4 v-36 h5 v36 h4 v-36 h5 v42 q0 16 -12 20 l-2 98 q0 6 -5 6 q-5 0 -5 -6 l-2 -98 q-12 -4 -12 -20 z"/>
      <ellipse cx="440" cy="740" rx="20" ry="32"/>
      <path d="M434 768 h12 l-1 104 q0 6 -5 6 q-5 0 -5 -6 z"/>
      <path d="M503 706 q14 20 12 82 l-6 4 l0 80 q0 6 -5 6 q-5 0 -5 -6 l-2 -150 q0 -14 6 -16 z"/>
    </g>
  </svg>

  <p class="course-list">SALADS, SOUPS, APPETIZERS,<br>PLATTERS, DESSERTS</p>
</main>
</body>
</html>
```